Design for sports training app

We need the design for 9 screens of an app that supports trainers of sport teams in preparing their training sessions. Regarding colors, fonts etc. there is absolute freedom for the designer to choose what he thinks is best.
The app will be called "Vellix", our idea for the logo is something like a stopwatch.
Wireframes are attached for every screen. You don't have to stick to those - if you have better ideas, we are happy to see them.
Our strategy is "mobile first". Based on the app design we will create a homepage later - I guess it makes sense to give this to the same person, let's see.
The deliverables are attached.
All in all the main target is to present a very simple, intuitive and nice UI that the user can work with without much learning.
Updates
Target Market(s)
Soccer trainers
Industry/Entity Type
Training
Look and feel

```html
<!DOCTYPE html>
<html lang="en">
<head>
<meta charset="utf-8">
<title>Vellix – Login</title>
<link rel="stylesheet" href="https://fonts.googleapis.com/css2?family=Open+Sans:wght@400;600;700&display=swap">
<style>
  :root {
    --field-bg: rgba(255,255,255,0.16);
    --field-border: rgba(255,255,255,0.55);
    --text-white: #ffffff;
    --placeholder: rgba(255,255,255,0.55);
    --icon-lilac: #9aa5f0;
    --button-blue: #243a8e;
    --grass-dark: #1d2a17;
    --grass-mid: #3a4f2a;
    --grass-light: #5d7046;
  }
  * { margin: 0; padding: 0; box-sizing: border-box; }
  html, body { width: 675px; height: 1200px; overflow: hidden; }
  body { font-family: "Open Sans", sans-serif; color: var(--text-white); background: var(--grass-dark); }
  .screen { position: relative; width: 675px; height: 1200px; overflow: hidden; }
  .backdrop {
    position: absolute; inset: 0;
    background:
      radial-gradient(ellipse 60% 40% at 50% 38%, rgba(40,30,30,0.55), transparent 70%),
      linear-gradient(180deg, #2f4122 0%, #3b4d2c 30%, var(--grass-light) 45%, var(--grass-mid) 70%, #4a5a3c 88%, #6b6b6e 100%);
    filter: brightness(0.78);
  }
  .status-bar {
    position: absolute; top: 0; left: 0; right: 0; height: 42px;
    display: flex; align-items: center; justify-content: space-between;
    padding: 0 12px; font-size: 19px;
  }
  .status-left { display: flex; align-items: center; gap: 8px; }
  .signal { display: flex; gap: 3px; }
  .signal span { width: 9px; height: 9px; border-radius: 50%; border: 1.5px solid #fff; }
  .signal span.on { background: #fff; }
  .status-right { display: flex; align-items: center; gap: 6px; }
  .battery { width: 36px; height: 17px; border: 1.5px solid #fff; border-radius: 3px; padding: 2px; position: relative; }
  .battery::after { content: ""; position: absolute; right: -5px; top: 4px; width: 3px; height: 6px; background: #fff; border-radius: 0 2px 2px 0; }
  .battery i { display: block; width: 100%; height: 100%; background: #fff; border-radius: 1px; }
  .status-time { position: absolute; left: 50%; transform: translateX(-50%); font-weight: 600; }
  .brand {
    position: absolute; top: 395px; left: 0; right: 0;
    display: flex; justify-content: center; align-items: center; gap: 14px;
  }
  .brand-dot { width: 22px; height: 22px; border-radius: 50%; background: var(--text-white); }
  .brand-name { font-size: 38px; font-weight: 700; letter-spacing: 4px; }
  .field {
    position: absolute; left: 36px; width: 604px; height: 69px;
    background: var(--field-bg); display: flex; align-items: center;
    padding-left: 18px; font-size: 26px;
  }
  .field-user { top: 615px; border: 1.5px solid var(--field-border); }
  .field-password { top: 703px; }
  .field svg { width: 38px; height: 38px; margin-right: 16px; flex: none; }
  .field-value { display: flex; align-items: center; }
  .caret { display: inline-block; width: 2px; height: 32px; background: #fff; margin-left: 4px; }
  .placeholder { color: var(--placeholder); }
  .login-button {
    position: absolute; top: 832px; left: 36px; width: 604px; height: 87px;
    background: var(--button-blue); border-radius: 2px;
    display: flex; align-items: center; justify-content: center;
    font-size: 25px; letter-spacing: 0.5px;
    box-shadow: 0 2px 6px rgba(0,0,0,0.35);
  }
  .account-links {
    position: absolute; top: 940px; left: 38px; right: 35px;
    display: flex; justify-content: space-between; font-size: 22px;
  }
</style>
</head>
<body>
<main class="screen">
  <div class="backdrop" role="img" aria-label="Soccer player controlling a ball on a training pitch with balls in the foreground, darkened"></div>

  <header class="status-bar">
    <div class="status-left">
      <div class="signal"><span class="on"></span><span class="on"></span><span class="on"></span><span></span><span></span></div>
      <span>Nordline</span>
      <svg width="22" height="16" viewBox="0 0 22 16" aria-hidden="true"><path d="M1 5a14 14 0 0 1 20 0M4.5 8.5a9 9 0 0 1 13 0M8 12a4 4 0 0 1 6 0" stroke="#fff" stroke-width="2" fill="none"/></svg>
    </div>
    <span class="status-time">4:21 PM</span>
    <div class="status-right"><span>100%</span><div class="battery"><i></i></div></div>
  </header>

  <div class="brand">
    <span class="brand-dot"></span>
    <span class="brand-name">VELLIX</span>
  </div>

  <div class="field field-user">
    <svg viewBox="0 0 38 38" aria-hidden="true"><circle cx="19" cy="12" r="8" fill="var(--icon-lilac)"/><path d="M3 36c0-9 7-14 16-14s16 5 16 14z" fill="var(--icon-lilac)"/></svg>
    <span class="field-value">Dara Mensel<span class="caret"></span></span>
  </div>

  <div class="field field-password">
    <svg viewBox="0 0 38 38" aria-hidden="true"><path d="M12 17v-5a7 7 0 0 1 14 0v5" stroke="var(--icon-lilac)" stroke-width="3" fill="none"/><rect x="8" y="16" width="22" height="20" rx="4" fill="var(--icon-lilac)"/></svg>
    <span class="placeholder">Password</span>
  </div>

  <div class="login-button">LOGIN</div>

  <nav class="account-links">
    <span>Forgot Password?</span>
    <span>Creat an Account</span>
  </nav>
</main>
</body>
</html>
```